Medien Firma benötigt Briefpapier
Zielgruppe
Firma:
Wir sind im Bereich Veranstaltungstechnik und Eventmanagement seit 2007 tätig. Ab 2009 konnten wir unsere Expertise um die Bereiche Medientechnik und TV Produktion erweitern. Durch dieses Portfolio sind wir in der Lage, alle Facetten der technischen Planung durchzuführen.
Bereiche:
Veranstaltungstechnik - Medientechnik - Livestreaming
Kunden:
B2B
Aufgabenstellung
Erstellung von Briefpapier mit dem vorhandenen Logo.
Das Briefpapier soll auch als Produktsheet nutzbar sein. Also muss der Footer Text austauschbar sein.
Schlicht, Modern, Zeitlos, max. zwei Farben

```html
<!DOCTYPE html>
<html lang="de">
<head>
<meta charset="utf-8">
<title>nordhallmedia – Briefpapier</title>
<link rel="stylesheet" href="https://fonts.googleapis.com/css2?family=Open+Sans:wght@300;400;600&display=swap">
<style>
  :root {
    --backdrop: #8fa0a7;
    --paper: #ffffff;
    --brand-blue: #049de0;
    --motif-tint: #e3f3fb;
    --rule-blue: #9fd4f0;
    --ink: #1c1c1c;
    --shadow: rgba(40, 55, 62, 0.28);
  }
  * { box-sizing: border-box; margin: 0; padding: 0; }
  html, body {
    width: 1200px; height: 971px; overflow: hidden;
    background: var(--backdrop);
    font-family: "Open Sans", Arial, sans-serif;
    color: var(--ink);
  }
  .stationery { position: relative; width: 1200px; height: 971px; }
  .sheet {
    position: absolute; top: 80px;
    width: 572px; height: 810px;
    background: var(--paper);
    box-shadow: 0 6px 18px var(--shadow);
    overflow: hidden;
  }
  .sheet--letter { left: 20px; }
  .sheet--product { left: 608px; }

  /* Letterhead */
  .sender-line {
    position: absolute; left: 62px; top: 62px;
    font-size: 5.5px; line-height: 1.5; color: var(--ink);
  }
  .sender-line .sender-name { color: var(--brand-blue); font-weight: 600; display: block; }
  .wordmark {
    position: absolute; display: flex; align-items: center;
    font-weight: 300; color: var(--ink); letter-spacing: -0.01em;
    white-space: nowrap;
  }
  .wordmark__dot {
    border: 1.2px solid var(--brand-blue); border-radius: 50%;
    flex: none;
  }
  .sheet--letter .wordmark { right: 58px; top: 120px; font-size: 22px; gap: 6px; }
  .sheet--letter .wordmark__dot { width: 14px; height: 14px; }

  .footer {
    position: absolute; left: 90px; right: 52px; bottom: 60px;
  }
  .footer__rule { height: 1px; background: var(--rule-blue); }
  .footer__columns {
    display: flex; gap: 70px; margin: 56px 0 0 50px;
    font-size: 6.5px; line-height: 1.55;
  }
  .footer__contact { font-style: normal; }
  .footer__columns a { color: var(--brand-blue); text-decoration: none; }

  /* Product sheet */
  .motif-area {
    position: absolute; left: 50px; top: 120px;
    width: 490px; height: 380px;
    background: linear-gradient(135deg, var(--motif-tint), #f4fafd);
  }
  .sheet--product .wordmark { left: 56px; bottom: 96px; font-size: 44px; gap: 10px; }
  .sheet--product .wordmark__dot { width: 26px; height: 26px; border-width: 2px; }
</style>
</head>
<body>
<main class="stationery">

  <section class="sheet sheet--letter" aria-label="Briefbogen">
    <p class="sender-line">
      <span class="sender-name">nordhallmedia</span>
      Musterstraße 1 | 12345 Musterstadt | info@nordhallmedia.de
    </p>

    <div class="wordmark"><span class="wordmark__dot"></span>nordhallmedia</div>

    <footer class="footer">
      <div class="footer__rule"></div>
      <div class="footer__columns">
        <address class="footer__contact">
          Musterstraße 1<br>
          12345 Musterstadt<br>
          Tel. 0123 456 789<br>
          info@nordhallmedia.de<br>
          <a href="#">www.nordhallmedia.de</a>
        </address>
        <p class="footer__bank">
          Finanzamt Musterstadt<br>
          Ust-ID: DE 123 456 789<br>
          BV: Musterbank<br>
          BIC: ABCDEFGH<br>
          IBAN: DE 1234 5678 9012 3456 7890
        </p>
      </div>
    </footer>
  </section>

  <section class="sheet sheet--product" aria-label="Produktblatt Rückseite">
    <div class="motif-area" role="img" aria-label="Fläche für das große Markenmotiv in Blau und Weiß"></div>
    <div class="wordmark"><span class="wordmark__dot"></span>nordhallmedia</div>
  </section>

</main>
</body>
</html>
```